Business Card design for a company called Tully Brook Co

I need a business card design for my oil fired boiler servicing company. I have a logo design already and Im just looking that incorporated into the business card design. card details; Tully Brook Co
Oil Burner Servicing - Mid Ulster Area
Service Engineer - Owen Madler
Mobile 07700914862
email - Tully.Brook.Co@quillpost.net
www.tullybrookco.net
I carry out Servicing, Commissioning, Fault Finding, Warranty Validation
Target Market(s)
home owners with oil fired central heating
Industry/Entity Type
Business
Contact Information for Business Card
Tully Brook Co
Tell. 07700914862
Web: www.tullybrookco.net
email Tully.Brook.Co@Quillpost.Net
Servicing Fault Finding Commissioning Warranty Validation
Look and feel

```html
<!DOCTYPE html>
<html lang="en">
<head>
<meta charset="utf-8">
<title>Tully Brook Co – Business Card</title>
<link rel="stylesheet" href="https://fonts.googleapis.com/css2?family=Questrial&display=swap">
<style>
  :root {
    --green: #45b03a;
    --green-dark: #2f8a2c;
    --green-light: #7cc95a;
    --ink: #4a4a4a;
    --ink-soft: #707070;
    --paper: #ffffff;
    --paper-shade: #eeeeee;
    --stage: #e6e7e3;
  }
  * { box-sizing: border-box; margin: 0; padding: 0; }
  html, body { width: 1200px; height: 950px; overflow: hidden; }
  body {
    background: var(--stage);
    font-family: "Questrial", Arial, sans-serif;
    color: var(--ink);
    position: relative;
  }
  .card {
    position: absolute;
    left: 250px;
    width: 700px;
    height: 400px;
    border-radius: 4px;
    overflow: hidden;
    box-shadow: 0 6px 18px rgba(0,0,0,0.18);
  }

  /* Front */
  .card-front { top: 50px; background: linear-gradient(180deg, var(--paper) 60%, var(--paper-shade)); }
  .brand { position: absolute; left: 40px; top: 40px; display: flex; align-items: center; gap: 14px; }
  .brand-dot { width: 50px; height: 50px; border-radius: 50%; background: var(--green); }
  .brand-name { font-size: 36px; color: var(--green); line-height: 1; }
  .brand-tagline {
    position: absolute; left: 104px; top: 88px;
    font-size: 10px; letter-spacing: 2.2px; text-transform: uppercase; color: var(--green);
  }
  .divider { position: absolute; left: 40px; top: 214px; width: 420px; height: 1.5px; background: var(--green); }
  .contacts { position: absolute; left: 40px; top: 228px; list-style: none; }
  .contacts li { display: flex; align-items: center; gap: 10px; font-size: 18px; height: 26px; color: var(--ink); }
  .contacts svg { width: 16px; height: 16px; fill: var(--green); flex: none; }
  .person { position: absolute; right: 40px; top: 194px; text-align: right; }
  .person-name { font-size: 26px; line-height: 32px; color: var(--green); }
  .person-role { font-size: 19px; line-height: 24px; color: var(--ink-soft); }
  .services { position: absolute; right: 40px; top: 282px; list-style: none; text-align: right; }
  .services li { font-size: 18px; line-height: 23px; color: var(--ink-soft); }
  .services li::after {
    content: ""; display: inline-block; width: 7px; height: 7px; border-radius: 50%;
    background: var(--green); margin-left: 10px; vertical-align: middle;
  }
  .base-band {
    position: absolute; left: 0; bottom: 0; width: 100%; height: 20px;
    background: linear-gradient(90deg, var(--green-dark), var(--green) 35%, var(--green-light) 60%, var(--paper-shade) 80%);
  }
  .corner-mark {
    position: absolute; right: 180px; bottom: 4px; width: 28px; height: 28px; border-radius: 50%;
    background: var(--green); border: 3px solid var(--paper);
  }

  /* Back */
  .card-back {
    top: 500px;
    background: linear-gradient(100deg, var(--green-light), var(--green) 50%, var(--green-dark));
  }
  .back-brand {
    position: absolute; left: 0; right: 0; top: 120px;
    display: flex; flex-direction: column; align-items: center; gap: 18px;
  }
  .back-dot { width: 90px; height: 90px; border-radius: 50%; background: var(--paper); opacity: 0.9; }
  .back-name { font-size: 30px; color: var(--paper); }
  .back-social { position: absolute; left: 300px; bottom: 60px; display: flex; align-items: center; gap: 10px; }
  .social-dot { width: 18px; height: 18px; border-radius: 50%; background: rgba(255,255,255,0.75); }
  .social-line { width: 150px; height: 1px; background: rgba(255,255,255,0.75); }
</style>
</head>
<body>

<section class="card card-front" aria-label="Card front">
  <div class="brand">
    <span class="brand-dot"></span>
    <span class="brand-name">Tully Brook Co</span>
  </div>
  <p class="brand-tagline">Oil Burner Servicing - Mid Ulster Area</p>

  <div class="divider"></div>

  <ul class="contacts">
    <li>
      <svg viewBox="0 0 16 16" aria-hidden="true"><path d="M4 0h8a1 1 0 0 1 1 1v14a1 1 0 0 1-1 1H4a1 1 0 0 1-1-1V1a1 1 0 0 1 1-1zm1 2v10h6V2zm3 11a1 1 0 1 0 0 2 1 1 0 0 0 0-2z"/></svg>
      07700914862
    </li>
    <li>
      <svg viewBox="0 0 16 16" aria-hidden="true"><path d="M1 5c0-2 3-3 7-3s7 1 7 3v1h-4V4.5H5V6H1zM3 7h10l2 7H1z"/></svg>
      07700914862
    </li>
    <li>
      <svg viewBox="0 0 16 16" aria-hidden="true"><path d="M0 3h16v1L8 9 0 4zm0 3 8 5 8-5v7H0z"/></svg>
      Tully.Brook.Co@quillpost.net
    </li>
    <li>
      <svg viewBox="0 0 16 16" aria-hidden="true"><circle cx="8" cy="8" r="7.5"/><path d="M1 8h14M8 1c-4 4-4 10 0 14M8 1c4 4 4 10 0 14" stroke="#fff" stroke-width="1" fill="none"/></svg>
      www.tullybrookco.net
    </li>
  </ul>

  <div class="person">
    <p class="person-name">Owen Madler</p>
    <p class="person-role">Service Engineer</p>
  </div>

  <ul class="services">
    <li>Commissioning</li>
    <li>Fault Finding</li>
    <li>Warranty Validation</li>
  </ul>

  <div class="base-band"></div>
  <span class="corner-mark"></span>
</section>

<section class="card card-back" aria-label="Card back">
  <div class="back-brand">
    <span class="back-dot"></span>
    <span class="back-name">Tully Brook Co</span>
  </div>
  <div class="back-social">
    <span class="social-dot"></span>
    <span class="social-dot"></span>
    <span class="social-line"></span>
  </div>
</section>

</body>
</html>
```